Wendlow Cellars -responsive, bootstrap website design

Looking to build a responsive service website.

Logo and pictures have been provided.

PLEASE REVIEW ATTACHED DESIGN STYLE GUIDES & CLIENT CREATIVE BRIEF FOR OUR REQUIREMENT. THANK YOU AND GOOD LUCK!

```html
<!DOCTYPE html>
<html lang="en">
<head>
<meta charset="utf-8">
<title>Wendlow Cellars</title>
<link href="https://fonts.googleapis.com/css2?family=Noto+Serif:ital,wght@0,400;0,700;1,400;1,700&display=swap" rel="stylesheet">
<style>
:root{
  --header-bg:#241b15;
  --wood-dark:#4a3221;
  --wood-light:#7a5a3e;
  --gold:#c8913a;
  --wine:#a30f1d;
  --green:#6d8a16;
  --green-light:#8aa628;
  --page-bg:#f2efea;
  --white:#ffffff;
  --text:#333333;
  --footer-bg:#1c1c1c;
  --footer-bottom:#121212;
  --footer-text:#9a9a9a;
}
*{box-sizing:border-box;margin:0;padding:0}
html,body{width:1200px;height:2350px;overflow:hidden}
body{position:relative;background:var(--page-bg);font-family:"Noto Serif",Georgia,serif;color:var(--text)}
.abs{position:absolute}

/* header */
.site-header{position:absolute;left:0;top:0;width:1200px;height:243px;background:var(--header-bg)}
.logo{position:absolute;left:58px;top:22px;width:212px;height:163px;border:2px solid #d8d0c4;outline:1px solid #d8d0c4;outline-offset:-8px;display:flex;flex-direction:column;align-items:center;justify-content:center;color:#f2ece2}
.logo-name{font-size:30px;font-weight:400;text-align:center;line-height:1.15}
.logo-sub{font-size:10px;letter-spacing:1.5px;margin-top:14px;border-top:1px solid #d8d0c4;padding-top:6px}
.phone{position:absolute;right:58px;top:26px;color:#b9a78f;font-size:20px;display:flex;align-items:center;gap:8px}
.top-links{position:absolute;right:58px;top:84px;font-size:14px;color:var(--gold);display:flex;gap:10px;align-items:center;white-space:nowrap}
.top-links b{color:#fff;font-weight:400}
.top-links .dot{width:6px;height:6px;border-radius:50%;background:var(--gold)}
.join-btn{position:absolute;left:937px;top:138px;width:205px;height:44px;border:1px solid var(--gold);border-radius:4px;color:var(--gold);font-size:13px;font-style:italic;font-weight:700;display:flex;align-items:center;justify-content:center;white-space:nowrap}

.main-nav{position:absolute;left:58px;top:215px;width:1084px;height:62px;display:flex;gap:4px;z-index:2}
.main-nav a{height:62px;display:flex;align-items:center;justify-content:center;font-size:21px;color:#c9b393;text-decoration:none;background:linear-gradient(180deg,var(--wood-light),var(--wood-dark) 50%,#5d402a);border-bottom:3px solid #2b1d13}
.main-nav a.active{color:#fff}

/* hero */
.hero{position:absolute;left:0;top:243px;width:1200px;height:626px;background:radial-gradient(ellipse 640px 420px at 620px 300px,#7a0c12,#30050a 60%,#080101)}
.hero-badge{position:absolute;left:133px;top:423px;width:298px;height:298px;border-radius:50%;background:var(--white);border:6px solid var(--green);overflow:hidden}
.hero-badge .fill{position:absolute;left:0;top:0;width:100%;height:222px;background:var(--green);border-radius:0 0 50% 50%/0 0 30px 30px;display:flex;align-items:center;justify-content:center;text-align:center;color:#fff;font-size:29px;font-style:italic;font-weight:700;line-height:1.5;padding-top:18px}
.hero-badge .more{position:absolute;left:0;width:100%;top:240px;text-align:center;font-size:16px;font-weight:700;color:var(--wine)}

.promo-band{position:absolute;left:58px;top:869px;width:1084px;height:160px;background:linear-gradient(90deg,var(--green),var(--green-light) 50%,var(--green));display:flex;border-bottom:6px solid #4f6410}
.promo{flex:1;position:relative;padding:22px 0 0 22px;color:#fff}
.promo h3{font-size:19px;font-weight:700;line-height:1.3;width:250px}
.promo p{font-size:13px;margin-top:12px;line-height:1.45;width:250px}
.promo .view{position:absolute;left:176px;top:124px;font-size:14px;font-style:italic}
.promo .bottle{position:absolute;right:22px;top:8px;width:46px;height:146px;border-radius:16px 16px 6px 6px}

/* products */
.section-title{font-size:22px;font-weight:700;color:var(--wine)}
.feature-title{position:absolute;left:58px;top:1068px;width:1084px;display:flex;align-items:center;gap:14px}
.feature-title::after{content:"";flex:1;height:1px;background:var(--wine)}
.product{position:absolute;top:1108px;width:262px;height:366px;background:var(--white)}
.product .frame{position:absolute;left:11px;top:10px;width:240px;height:193px;border:1px solid var(--wine)}
.product .bottle{position:absolute;left:102px;top:14px;width:36px;height:166px;border-radius:12px 12px 4px 4px;background:linear-gradient(180deg,#7a1a26,#2a1215)}
.product .quick{position:absolute;left:65px;top:95px;width:110px;height:34px;background:var(--wine);border-radius:3px;color:#fff;font-size:14px;display:flex;align-items:center;justify-content:center}
.product .name{position:absolute;top:209px;left:14px;right:14px;text-align:center;font-size:14px;line-height:1.5;color:#555}
.product .price{position:absolute;top:265px;width:100%;text-align:center;font-size:20px;font-weight:700;color:var(--wine)}
.product .cart{position:absolute;top:308px;left:75px;width:110px;height:32px;border-radius:2px;background:#b5b5b5;color:#333;font-size:14px;display:flex;align-items:center;justify-content:center}
.product .cart.primary{background:var(--wine);color:#fff;font-weight:700}

/* media panel */
.media-panel{position:absolute;left:58px;top:1507px;width:1084px;height:580px;background:var(--white)}
.thumb{position:absolute;height:128px}
.play{position:absolute;left:50%;top:50%;width:52px;height:52px;margin:-26px 0 0 -26px;border:3px solid #fff;border-radius:50%}
.play::after{content:"";position:absolute;left:19px;top:13px;border-left:16px solid #fff;border-top:10px solid transparent;border-bottom:10px solid transparent}
.news{position:absolute;top:1912px;width:230px}
.news .date{font-size:16px;font-weight:700;color:var(--wine)}
.news h4{font-size:14px;font-weight:700;color:#111;margin-top:10px}
.news p{font-size:13px;color:#555;line-height:1.5;margin-top:8px}
.more-news{position:absolute;left:81px;top:2024px;width:115px;height:30px;background:var(--wine);color:#fff;font-size:14px;display:flex;align-items:center;justify-content:center}

/* footer */
.site-footer{position:absolute;left:0;top:2087px;width:1200px;height:219px;background:var(--footer-bg)}
.foot-col{position:absolute;top:14px}
.foot-col h5{font-size:20px;font-weight:400;color:#e8e8e8;margin-bottom:14px}
.foot-col li{list-style:none;font-size:15px;color:var(--footer-text);height:33px}
.foot-col li.active{color:#fff}
.social li{display:flex;gap:12px;align-items:flex-start;height:36px}
.social .sq{width:24px;height:24px;background:#555}
.footer-bottom{position:absolute;left:0;top:2306px;width:1200px;height:44px;background:var(--footer-bottom);color:var(--footer-text);font-size:14px;padding:14px 0 0 56px}
</style>
</head>
<body>

<header class="site-header">
  <div class="logo">
    <div class="logo-name">Wendlow<br>Cellars</div>
    <div class="logo-sub">HOLLIN RIDGE VALLEY</div>
  </div>
  <div class="phone">
    <svg width="20" height="20" viewBox="0 0 24 24"><path d="M6.6 10.8c1.4 2.8 3.8 5.1 6.6 6.6l2.2-2.2c.3-.3.7-.4 1-.2 1.1.4 2.3.6 3.6.6.6 0 1 .4 1 1V20c0 .6-.4 1-1 1C10.6 21 3 13.4 3 4c0-.6.4-1 1-1h3.5c.6 0 1 .4 1 1 0 1.3.2 2.5.6 3.6.1.3 0 .7-.2 1z" fill="#b9703a"/></svg>
    555.014.2290
  </div>
  <nav class="top-links">
    <b>Cart :</b><span>O Item(s): 0</span><span class="dot"></span><span>Wish list (0)</span><span class="dot"></span><span>My account</span><span class="dot"></span><span>Shopping Cart</span><span class="dot"></span><span>Checkout</span>
  </nav>
  <div class="join-btn">Join The Wendlow Family</div>
</header>

<nav class="main-nav">
  <a class="active" style="width:169px">Home</a>
  <a style="width:195px">About Us</a>
  <a style="width:172px">Wines</a>
  <a style="width:155px">Store</a>
  <a style="width:155px">News</a>
  <a style="width:218px">Contact Us</a>
</nav>

<section class="hero" role="img" aria-label="Illustration of a wine bottle, a glass of red wine and bunches of grapes on a dark red background"></section>
<div class="hero-badge">
  <div class="fill">WENDLOW<br>CELLARS<br>HOLLIN RIDGE</div>
  <div class="more">More detalis</div>
</div>

<section class="promo-band">
  <div class="promo">
    <h3>2011 Wendlow Cellars Cabernet Sauvignon</h3>
    <p>Vulputate sit amet posuere Rutrum at neque placerat o</p>
    <span class="view">View all ›</span>
    <div class="bottle" role="img" aria-label="Bottle of white wine" style="background:linear-gradient(180deg,#e4e8c8,#b8c27a)"></div>
  </div>
  <div class="promo">
    <h3>2011 Wendlow Cellars Cabernet Sauvignon</h3>
    <p>Mattis leo lorem ullamcorper ipsum Mattis leo lorem ullamc</p>
    <span class="view">View all ›</span>
    <div class="bottle" role="img" aria-label="Bottle of red wine" style="background:linear-gradient(180deg,#4a2a2a,#2a1418)"></div>
  </div>
  <div class="promo">
    <h3>2011 Wendlow Cellars Cabernet Sauvignon</h3>
    <p>Aipiscing ipsum mattis vitae voltpat urna dignissimliquam</p>
    <span class="view">View all ›</span>
    <div class="bottle" role="img" aria-label="Bottle of red wine" style="background:linear-gradient(180deg,#7a1424,#2a1418)"></div>
  </div>
</section>

<h2 class="feature-title section-title">Feature Product</h2>

<article class="product" style="left:58px">
  <div class="frame"><div class="bottle" role="img" aria-label="Bottle of Cabernet Sauvignon"></div><div class="quick">Quick View</div></div>
  <div class="name">2011 Wendlow Cellars Cabernet Sauvignon</div>
  <div class="price">$34.00</div>
  <div class="cart primary">Add to Cart</div>
</article>
<article class="product" style="left:332px">
  <div class="frame"><div class="bottle" role="img" aria-label="Bottle of Cabernet Sauvignon"></div></div>
  <div class="name">2011 Wendlow Cellars Cabernet Sauvignon Magnum</div>
  <div class="price">$79.00</div>
  <div class="cart">Add to Cart</div>
</article>
<article class="product" style="left:606px">
  <div class="frame"><div class="bottle" role="img" aria-label="Bottle of Cabernet Sauvignon"></div></div>
  <div class="name">2011 Wendlow Cellars Cabernet Sauvignon 3-Liter</div>
  <div class="price">$250.00</div>
  <div class="cart">Add to Cart</div>
</article>
<article class="product" style="left:880px">
  <div class="frame"><div class="bottle" role="img" aria-label="Bottle of Cabernet Sauvignon"></div></div>
  <div class="name">2011 Wendlow Cellars Cabernet Sauvignon 6-Liter</div>
  <div class="price">$375.00</div>
  <div class="cart">Add to Cart</div>
</article>

<section class="media-panel"></section>
<h2 class="section-title abs" style="left:80px;top:1522px">Latest Video</h2>
<h2 class="section-title abs" style="left:332px;top:1516px">Photo Gallery</h2>

<div class="thumb" role="img" aria-label="Video still of wine bottles on a dark shelf" style="left:80px;top:1567px;width:218px;background:linear-gradient(180deg,#1c1c1c,#3a3434)"><span class="play"></span></div>
<div class="thumb" role="img" aria-label="Video still of wine bottles at a tasting table" style="left:80px;top:1717px;width:218px;background:linear-gradient(180deg,#3a3230,#6a5a50)"><span class="play"></span></div>

<div class="thumb" role="img" aria-label="Photo of a labelled wine bottle outdoors" style="left:332px;top:1567px;width:248px;background:linear-gradient(90deg,#3a3a28,#6a5a48 50%,#2a2a22)"></div>
<div class="thumb" role="img" aria-label="Photo of a row of wine bottles" style="left:603px;top:1567px;width:248px;background:linear-gradient(180deg,#d8d4cc,#4a3438)"></div>
<div class="thumb" role="img" aria-label="Photo of the winemaker in the vineyard" style="left:873px;top:1567px;width:248px;background:linear-gradient(180deg,#6a7040,#3a3a2a)"></div>
<div class="thumb" role="img" aria-label="Photo of bottles at a tasting bar" style="left:332px;top:1717px;width:248px;background:linear-gradient(180deg,#9a9896,#2a2a2a)"></div>
<div class="thumb" role="img" aria-label="Photo of a wine tasting table with food" style="left:603px;top:1717px;width:248px;background:linear-gradient(180deg,#7a5a48,#3a3a5a)"></div>
<div class="thumb" role="img" aria-label="Photo of wine bottles and cases on a table" style="left:873px;top:1717px;width:248px;background:linear-gradient(180deg,#6a7a4a,#6a4a2a)"></div>

<h2 class="section-title abs" style="left:80px;top:1872px">Latest News</h2>
<div class="news" style="left:80px"><div class="date">10.10.2014</div><h4>Lorem ipsum dolor sit amet</h4><p>Cetur adipiscing elitivam mollis facilisisraesent.</p></div>
<div class="news" style="left:349px"><div class="date">10.10.2014</div><h4>Lorem ipsum dolor sit amet</h4><p>Cetur adipiscing elitivam mollis facilisistraesent.</p></div>
<div class="news" style="left:620px"><div class="date">10.10.2014</div><h4>Lorem ipsum dolor sit amet</h4><p>Cetur adipis cing elitivam mollis facilisisraesent.</p></div>
<div class="news" style="left:912px"><div class="date">10.10.2014</div><h4>Lorem ipsum dolor sit amet</h4><p>Cetur adipiscing elitivam mollis facilisisraesent.</p></div>
<div class="more-news">More News</div>

<footer class="site-footer">
  <div class="foot-col" style="left:56px"><h5>Menu</h5><ul><li class="active">Home</li><li>About Us</li><li>Wine</li><li>Store</li><li>News</li></ul></div>
  <div class="foot-col" style="left:337px"><h5>Why buy from us</h5><ul><li>Shipping &amp; Returns</li><li>Secure Shopping</li><li>International Shipping</li><li>Affiliates</li><li>Group Sales</li></ul></div>
  <div class="foot-col" style="left:692px"><h5>My account</h5><ul><li>Specials</li><li>New products</li><li>Obest sellers</li><li>Pages configuration</li><li>Sitemap</li></ul></div>
  <div class="foot-col social" style="left:1031px"><h5>Follow us</h5><ul><li><span class="sq"></span>Friendly</li><li><span class="sq"></span>Chirper</li><li><span class="sq"></span>Picturely</li></ul></div>
</footer>
<div class="footer-bottom">Copyright © 2014 Wendlow Cellars. All Rights Reserved.</div>

</body>
</html>
```